Word Document Estimate Sheet

Good evening. I have an home renovations company that does a lot of estimates through word documents and then emailed them a PDF document. ArtHarbor did my logo and stationary projects and did a great job with it. Now I need my word document estimate sheet to be more standardized meaning sometimes my headers and footers move when I get to the bottom of the page , this make me have to do a copy and paste many times to put them back in their place also I have headings like Master Bedroom, Master Bath . I would like for them to always be bold, underlined and colon on the end now I always have to do this. I would like for the header and footers to not move when I get to the bottom of the page. Basically I want the same document with the same look as the document I send but with less retyping and copy and pasting. Hopefully this makes sense and you can help my estimates go faster.

Thanks,
Glen

Target Market(s)

Customer who want an estimate

Industry/Entity Type

It Company

Requirements
Must have
• 1.Must have same header and footer as the document I sent but want text to be standard.
• 2.Header and footer must not move when I get to the bottom of page.
• 3.Categories like Master Bedroom, Kitchen Area categories must already be in the document and if I want to delete them I can.
Nice to have
• I would love my estimate time to be cut in half because new word estimate sheet is simple to work with.
Should not have
• Don't change the header and footer design at all just make sure it doesn't move when I type.

```html
<!DOCTYPE html>
<html lang="en">
<head>
<meta charset="utf-8">
<title>Estimate Sheet – Kessler Home Renovations</title>
<link href="https://fonts.googleapis.com/css2?family=Tinos:wght@400;700&display=swap" rel="stylesheet">
<style>
  :root {
    --header-grey: #e1e1e1;
    --rule-navy: #1c3557;
    --footer-navy: #1a0f4d;
    --brand-navy: #1e1a5c;
    --alert-red: #ff0000;
    --ink: #111111;
    --cell-grey: #e2e2e2;
    --line: #444444;
    --white: #ffffff;
  }
  * { margin: 0; padding: 0; box-sizing: border-box; }
  html, body { width: 848px; height: 1200px; overflow: hidden; background: var(--white); }
  body { font-family: "Tinos", "Times New Roman", serif; color: var(--ink); }
  .sheet { position: relative; width: 848px; height: 1200px; }

  .page-header { position: absolute; left: 0; top: 0; width: 848px; height: 118px; background: var(--header-grey); }
  .page-header::after { content: ""; position: absolute; left: 0; top: 118px; width: 848px; height: 9px; background: var(--rule-navy); }
  .brand { position: absolute; left: 0; right: 0; top: 44px; display: flex; justify-content: center; align-items: center; gap: 10px; }
  .brand-mark { width: 16px; height: 16px; background: var(--brand-navy); }
  .brand-name { font-weight: 700; font-size: 24px; color: var(--brand-navy); letter-spacing: 0.5px; }

  .notes { position: absolute; left: 61px; width: 726px; top: 168px; color: var(--alert-red); font-weight: 700; font-size: 21px; line-height: 26px; }
  .notes p + p { margin-top: 18px; text-align: justify; text-align-last: left; }

  .completion { position: absolute; left: 53px; width: 742px; top: 328px; height: 54px; border-top: 1px solid var(--line); border-bottom: 1px solid var(--line); font-weight: 700; font-size: 24px; line-height: 52px; padding-left: 8px; }
  .completion .days { margin-left: 42px; }

  .cost-table { position: absolute; left: 53px; top: 409px; width: 742px; height: 154px; border-collapse: collapse; }
  .cost-table td, .cost-table th { border: 1px solid var(--line); }
  .cost-table th { height: 60px; font-size: 19px; font-weight: 400; line-height: 25px; }
  .cost-table .total-head { width: 341px; background: var(--cell-grey); font-weight: 700; font-size: 24px; line-height: 29px; }
  .cost-table .total-cell { background: var(--cell-grey); font-weight: 700; font-size: 28px; padding-left: 111px; }
  .cost-table td { font-weight: 700; font-size: 21px; }
  .cost-table .due-start { width: 192px; padding-left: 53px; }
  .cost-table .due-end { padding-left: 61px; }

  .payment-heading { position: absolute; left: 61px; top: 608px; font-weight: 700; font-size: 21px; }

  .terms { position: absolute; left: 61px; width: 726px; top: 839px; }
  .terms h2 { font-size: 21px; font-weight: 700; text-decoration: underline; }
  .terms ul { list-style: none; margin-top: 4px; }
  .terms li { position: relative; padding-left: 40px; font-size: 15px; line-height: 20px; margin-bottom: 5px; text-align: justify; }
  .terms li::before { content: ""; position: absolute; left: 15px; top: 8px; width: 5px; height: 5px; border-radius: 50%; background: var(--ink); }

  .thanks { position: absolute; left: 61px; top: 1003px; font-weight: 700; font-size: 23px; }

  .page-footer { position: absolute; left: 0; top: 1086px; width: 848px; height: 114px; background: var(--footer-navy); color: var(--white); text-align: center; font-size: 13.5px; line-height: 20.5px; padding-top: 22px; }
  .page-footer .site { font-weight: 700; font-size: 14px; }
</style>
</head>
<body>
<div class="sheet">
  <header class="page-header">
    <div class="brand">
      <span class="brand-mark"></span>
      <span class="brand-name">Kessler Home Renovations</span>
    </div>
  </header>

  <section class="notes">
    <p>Customer will select what color of paint to use in bathroom.</p>
    <p>All window seals “only” (No side frames) will be painted a semi-gloss white per the customer instructions.</p>
  </section>

  <div class="completion">Completion of job :<span class="days">Days</span></div>

  <table class="cost-table">
    <tr>
      <th class="total-head">Total cost for<br>labor &amp; materials:</th>
      <th>Due before<br>start of job:</th>
      <th>Due at<br>completion of job:</th>
    </tr>
    <tr>
      <td class="total-cell">$</td>
      <td class="due-start">$</td>
      <td class="due-end">$</td>
    </tr>
  </table>

  <h2 class="payment-heading">We Accepts These Forms of Payment:</h2>

  <section class="terms">
    <h2>Terms &amp; Conditions:</h2>
    <ul>
      <li>This is an estimate only, not a contract.</li>
      <li>This estimate is for completing the job described above, based on our evaluation.</li>
      <li>It does not include unforeseen price increases or additional labor and materials which may be required should problems arises.</li>
    </ul>
  </section>

  <p class="thanks">Thanks for your patronage of Kessler Home Renovations!!</p>

  <footer class="page-footer">
    <div class="site">www.kesslerhomereno.com</div>
    <div>Dana Kessler Office : 555-210-4417 &nbsp;|&nbsp; Glen Kessler Cell : 555-210-4418 &nbsp;|&nbsp; E-Mail: glen@kesslerhomereno.com</div>
    <div>412 North Maple St., Suite 210 Riverton, NC 28000</div>
  </footer>
</div>
</body>
</html>
```